Brookvale Systems Yellow rose letterhead

I have a new logo for my company but in its current form it is too large to be used on letterhead or as a email signature. I need to have the designer use elements from the current logo and create something close to the original but more suited for smaller items.
Updates

I just uploaded a copy of our logo that does not have the weathered affect. Thanks

Industry/Entity Type

It Company

Requirements
Must have
• The design must maintain the visual effect of the current logo. It needs to include the yellow rose and the name of the company.
Nice to have
• It would be nice to maintain the stamp theme and incorporate my name, address, phone, email. etc.

```html
<!DOCTYPE html>
<html lang="en">
<head>
<meta charset="utf-8">
<title>Brookvale Systems Letterhead</title>
<link rel="stylesheet" href="https://fonts.googleapis.com/css2?family=Open+Sans:wght@400;600;700&display=swap">
<style>
  :root {
    --backdrop: #8a8a8a;
    --paper: #f4f4f2;
    --band: #4a4039;
    --band-light: #5a5048;
    --gold: #f2b705;
    --cyan: #7fd3d8;
    --cream: #f1ece2;
    --ink: #2f2f2f;
    --sign-tone: #c9cfe6;
  }
  * { margin: 0; padding: 0; box-sizing: border-box; }
  html, body {
    width: 1200px; height: 900px; overflow: hidden;
    background: var(--backdrop);
    font-family: "Open Sans", Arial, sans-serif;
  }
  .letterhead {
    position: absolute; left: 290px; top: 12px;
    width: 620px; height: 876px;
    background: var(--paper);
    box-shadow: 0 6px 18px rgba(0,0,0,.28);
  }
  .masthead {
    position: relative; height: 118px;
    background: radial-gradient(ellipse at 30% 40%, var(--band-light), var(--band) 70%);
    border-bottom: 4px solid var(--gold);
  }
  .brand {
    position: absolute; left: 44px; top: 34px;
    display: flex; align-items: flex-start; gap: 14px;
  }
  .brand-mark {
    width: 48px; height: 48px; background: var(--gold); margin-top: 2px;
  }
  .brand-name {
    font-size: 26px; font-weight: 600; color: var(--cyan);
    letter-spacing: .5px; line-height: 1;
  }
  .brand-tagline {
    margin-top: 6px; color: var(--cream); line-height: 1.2;
  }
  .brand-tagline .motto { font-size: 10px; font-weight: 700; letter-spacing: 1.2px; text-transform: uppercase; }
  .brand-tagline .claim { font-size: 9px; }
  .sender {
    position: absolute; right: 40px; top: 30px;
    text-align: right; font-size: 8.5px; line-height: 1.35; color: var(--cream);
    font-style: normal;
  }
  .sender .sender-name { color: var(--gold); font-weight: 700; }
  .letter {
    padding: 48px 62px 0 62px;
    font-size: 11px; line-height: 1.55; color: var(--ink);
  }
  .recipient { margin-bottom: 18px; }
  .salutation { margin-bottom: 16px; }
  .letter p.body { margin-bottom: 16px; text-align: justify; }
  .signature {
    width: 150px; height: 38px; margin-top: 18px;
    background: linear-gradient(90deg, var(--sign-tone), rgba(201,207,230,0));
    border-radius: 4px;
  }
  .closing { margin-top: 4px; }
</style>
</head>
<body>
  <main class="letterhead">
    <header class="masthead">
      <div class="brand">
        <div class="brand-mark"></div>
        <div>
          <div class="brand-name">Brookvale Systems</div>
          <div class="brand-tagline">
            <div class="motto">Built on Clear Records</div>
            <div class="claim">Shaping Useful Insight for<br>Growing Local Firms</div>
          </div>
        </div>
      </div>
      <address class="sender">
        <div class="sender-name">Mara Quinlan, PhD</div>
        <div>410 Harlow Ridge Rd Ste 200</div>
        <div>Fernhill, TX 70000</div>
        <div>hello@brookvalesystems.com</div>
        <div>1 800 555 0142</div>
      </address>
    </header>

    <section class="letter">
      <div class="recipient">Dana Whitfield<br>82 Larchmont Ave<br>Eastbrook MA</div>
      <p class="salutation">Dear Mrs Dana Whitfield,</p>
      <p class="body">Lorem ipsum dolor sit amet, consectetur adipiscing elit. Integer aliquet diam eget mi rutrum consectetur et id orci. Praesent vitae felis vitae justo elementum tincidunt. Duis pharetra turpis semper dui elementum nec aliquet lectus pulvinar. Donec condimentum mattis diam, id congue risus congue a. Maecenas commodo, nisi a gravida condimentum, elit erat condimentum leo, in pellentesque elit erat id nisi. Pellentesque consequat faucibus dictum. Nam tincidunt viverra elit at hendrerit. Quisque eget purus tellus. Mauris mattis nunc nec nisi pulvinar consectetur.</p>
      <p class="body">Nunc molestie iaculis orci, vitae consequat mi condimentum vitae. Etiam et tortor velit. Sed ac magna tellus. Proin quam augue, vehicula sed euismod in, vehicula eu felis. Pellentesque a orci ac turpis commodo varius at ut arcu. Integer viverra semper sapien fermentum egestas. Curabitur erat purus, congue et faucibus sit amet, fringilla elementum odio. Sed pretium tincidunt mi, nec fermentum urna interdum sed. Nam et lectus turpis, quis cursus ipsum. Maecenas non nibh odio. Sed in laoreet justo.</p>
      <p class="body">Aenean sed sem lacus. Vivamus auctor, sapien non aliquet ultrices, mauris turpis porttitor nisl, id rutrum velit erat non urna. Praesent eu augue eu ligula feugiat malesuada. Proin nec nibh erat. Sed et leo id leo volutpat viverra non ac mi. In quis dictum magna. Donec ut dui sed dui tristique dictum. Donec varius sapien sed turpis dictum a dignissim diam facilisis.</p>
      <div class="signature" role="img" aria-label="Handwritten signature of Mara Quinlan"></div>
      <p class="closing">Yours Sincerely<br>Mara Quinlan</p>
    </section>
  </main>
</body>
</html>
```